Menu Design Project

Need a dine in menu for italian restaurant

Target Market(s)

30-60 years olds

Industry/Entity Type

Italian Restaurant

Colors

Designer to choose colors to be used in the design.

Requirements
Must have
• Breaf description for each item
Nice to have
• Some pictures
Should not have
• N/А

```html
<!DOCTYPE html>
<html lang="en">
<head>
<meta charset="utf-8">
<title>Italian Dine-In Menu</title>
<link rel="stylesheet" href="https://fonts.googleapis.com/css2?family=Arimo:wght@400;700&family=Yellowtail&family=Kalam:wght@700&display=swap">
<style>
:root{
  --stage:#4a4a4a;
  --board:#141414;
  --board-light:#222;
  --ink:#ffffff;
  --muted:#dcdcdc;
  --pink:#d95aa8;
  --label:#1e1e1e;
  --plate:#efefef;
}
*{box-sizing:border-box;margin:0;padding:0}
html,body{width:932px;height:1200px;overflow:hidden;background:var(--stage)}
body{position:relative;font-family:Arimo,Arial,sans-serif;color:var(--ink)}
.side-label{position:absolute;left:874px;font-family:Arimo,sans-serif;font-size:26px;letter-spacing:2px;color:var(--label);writing-mode:vertical-rl}
.side-label--outside{top:34px}
.side-label--inside{top:614px}
.panel{position:absolute;left:18px;width:800px;height:565px;overflow:hidden}
.panel--outside{top:35px}
.panel--inside{top:618px;background:linear-gradient(180deg,#1a1a1a,#101010)}
.cover-photo{position:absolute;inset:0;background:radial-gradient(ellipse at 55% 35%,#6b5a44 0%,#3a332b 35%,#1c1c1c 70%,var(--board) 100%)}
.photo{position:absolute;border-radius:50%}
.title-frame{position:absolute;left:444px;top:445px;width:276px;height:84px;border:2px solid var(--ink);border-top:none}
.title-frame::before,.title-frame::after{content:"";position:absolute;top:0;height:2px;background:var(--ink)}
.title-frame::before{left:0;width:18px}
.title-frame::after{right:0;width:18px}
.title-food{position:absolute;left:158px;top:-18px;font-size:29px;letter-spacing:1px;color:var(--ink);line-height:1}
.title-menu{position:absolute;left:14px;top:-14px;font-family:Yellowtail,"Brush Script MT",cursive;font-size:92px;color:var(--pink);line-height:1}
.heading{position:absolute;font-family:Kalam,cursive;font-style:italic;font-size:24px;letter-spacing:1px;color:var(--pink);line-height:1}
.item{position:absolute;font-size:7.6px;font-weight:700;line-height:1.15}
.col-app{left:194px;width:202px}
.col-sal{left:20px;width:178px}
.col-p1{left:410px;width:180px}
.col-p2{left:602px;width:180px}
.row{display:flex;align-items:baseline}
.dots{flex:1;border-bottom:1px dotted var(--ink);margin:0 1px}
.desc{font-size:6px;font-weight:700;color:var(--muted);line-height:1.2}
.note{position:absolute;font-size:6.8px;font-weight:700;color:var(--pink);line-height:1.2;text-transform:uppercase}
.dressings{position:absolute;left:20px;top:510px;width:178px;font-size:6.6px;font-style:italic;color:var(--pink);line-height:1.2}
.wings{display:grid;grid-template-columns:1fr 82px;column-gap:4px}
.wing-prices .row{font-size:7px}
</style>
</head>
<body>
<div class="side-label side-label--outside">OUTSIDE</div>
<div class="side-label side-label--inside">INSIDE</div>

<section class="panel panel--outside">
  <div class="cover-photo" role="img" aria-label="Tabletop photo of pizza, salads, fries, dip, beer and cutlery on dark wood"></div>
  <div class="title-frame">
    <span class="title-food">FOOD</span>
    <span class="title-menu">Menu</span>
  </div>
</section>

<section class="panel panel--inside">
  <div class="photo" role="img" aria-label="Grilled shrimp with chili pepper and dip" style="left:-50px;top:-2px;width:272px;height:272px;background:radial-gradient(#c2552e 30%,#7b2f1e 60%,#2a2a2a)"></div>
  <div class="photo" role="img" aria-label="Plate of pesto fettuccine" style="left:589px;top:-2px;width:208px;height:208px;background:radial-gradient(#a7a046 30%,#d9d3a8 45%,var(--plate) 60%)"></div>
  <div class="photo" role="img" aria-label="Bowl of grilled chicken salad with spinach and vegetables" style="left:206px;top:342px;width:192px;height:192px;background:radial-gradient(#d9a23a 25%,#3e6b2c 55%,#2a3a4a 75%)"></div>

  <h2 class="heading" style="left:194px;top:18px">APPETIZERS</h2>
  <h2 class="heading" style="left:418px;top:18px">PASTA</h2>
  <h2 class="heading" style="left:20px;top:294px">SALADS</h2>

  <div class="item col-app" style="top:56px"><div class="row">MOZZARELLA STICKS –(6)<span class="dots"></span>8.99</div></div>
  <div class="item col-app wings" style="top:68px">
    <div>BUFFALO CHICKEN WINGS<div class="desc">Hot, Extra Hot, Honey Bbq, Cajun Lemon Pepper, Teriyaki, TGarlic Parmesan</div></div>
    <div class="wing-prices"><div class="row">5pc<span class="dots"></span>5.99</div><div class="row">15pc<span class="dots"></span>15.99</div><div class="row">20pc<span class="dots"></span>20.99</div></div>
  </div>
  <div class="item col-app" style="top:111px"><div class="row">FRIED CALAMARI<span class="dots"></span>10.5</div></div>
  <div class="item col-app" style="top:128px"><div class="row">CHEESY BREAD<span class="dots"></span>9.99</div><div class="desc">10"pizza pie brushed with garlic sauce, topped with extra mozzarella cheese and served with marinara sauce</div></div>
  <div class="item col-app" style="top:158px"><div class="row">LOADED POTATO SKINS<span class="dots"></span>9.99</div><div class="desc">topped with bacon, cheddar cheese and mozzarella cheese with a side of sour cream)</div><div class="row">BUTTERFLY SHRIMP<span class="dots"></span>8.99</div></div>
  <div class="item col-app" style="top:206px"><div class="row">CHICKEN TENDERS(5)<span class="dots"></span>8.99</div></div>
  <div class="item col-app" style="top:222px"><div class="row">GARLIC BREAD TWISTS – (8)<span class="dots"></span>8.99</div><div class="desc">(Served with marinara Sauce)</div></div>
  <div class="item col-app" style="top:249px"><div class="row">JALAPENO PEPPERS (BREADED AND FRIED) (6)<span class="dots"></span>6.99</div></div>
  <div class="item col-app" style="top:266px"><div class="row">APPETIZER COMBO<span class="dots"></span>14.99</div><div class="desc">3potato skins, 3 mozzarella sticks, 2 chicken tenders, 3 jalapeno peppers</div></div>
  <p class="note" style="left:194px;top:293px;width:210px">Add grilled chicken (5oz)-$3.00, add fried chicken (5oz)-$3.00, add grilled salmon (6oz)-$4.99.</p>

  <div class="item col-sal" style="top:333px"><div class="row">HOUSE SALAD<span class="dots"></span>8.99</div><div class="desc">(ettuce, tomatoes, onions, bell peppers, black olives, mozzarella and cheddar cheese)</div></div>
  <div class="item col-sal" style="top:368px"><div class="row">CAESAR SALAD<span class="dots"></span>8.99</div><div class="desc">crisp romaine lettuce, parmesan cheese, croutons and caesar dressing)</div></div>
  <div class="item col-sal" style="top:402px"><div class="row">ANTIPASTO SALAD<span class="dots"></span>9.99</div><div class="desc">house salad with rolled salami, ham)</div></div>
  <div class="item col-sal" style="top:427px"><div class="row">GREEK SALAD<span class="dots"></span>8.99</div><div class="desc">(lettuce, tomatoes, black olives, feta cheese, onions, bell peppers and pepperoncini)</div></div>
  <div class="item col-sal" style="top:462px"><div class="row">COBB SALAD<span class="dots"></span>8.99</div><div class="desc">(lettuce, tomatoes, black olives, egg, bacon, mozzarella and cheddar cheese)</div></div>
  <div class="item col-sal" style="top:496px"><div class="row">SIDE SALAD<span class="dots"></span>4.99</div></div>
  <p class="dressings">Dressings: Ranch, Honey Mustard, Italian, Balsamic Vinagrette, Greek, French, Caesar, 1000 Island, Blue Cheese.</p>

  <div class="item col-p1" style="top:69px"><div class="row">MEAT LASAGNA<span class="dots"></span>15.99</div><div class="desc">(layers of pasta, beef, mozzarella&amp;ricotta cheeses topped with our tomato sauce</div></div>
  <div class="item col-p1" style="top:102px"><div>SPAGHETTI WITH MEATBALLS OR MEAT</div><div class="row">SAUCE<span class="dots"></span>15.99</div><div class="desc">(meatballs or meat sauce, tomato sauce, cheese and spaghetti)</div></div>
  <div class="item col-p1" style="top:146px"><div class="row">SPAGHETTI BOLOGNESE<span class="dots"></span>15.99</div><div class="desc">(homemade meat sauce with red wine, finely chopped onions over spaghetti)</div></div>
  <div class="item col-p1" style="top:180px"><div class="row">RAVIOLLI WITH MEAT OR CHEESE<span class="dots"></span>15.99</div><div class="desc">(pasta stuffed with meat or cheese and topped with marinara sauce)</div></div>
  <div class="item col-p1" style="top:214px"><div class="row">TORTELLINI WITH MEAT OR CHEESE<span class="dots"></span>15.99</div><div class="desc">(pasta stuffed with meat or cheese and topped with marinara sauce)</div></div>
  <div class="item col-p1" style="top:248px"><div class="row">TORTELLINI AURORA<span class="dots"></span>15.99</div><div class="desc">tortellini with mixture of alfredo &amp; marinara sauces)</div></div>
  <div class="item col-p1" style="top:274px"><div class="row">CHICKEN ALFREDO<span class="dots"></span>15.99</div><div class="desc">(ALFREDO SAUCE, CHICKEN, SEASONING AND FETTUCCINE)</div></div>
  <div class="item col-p1" style="top:308px"><div class="row">CAJUN CHICKEN ALFREDO<span class="dots"></span>15.99</div><div class="desc">(ALFREDO SAUCE, CHICKEN, CAJUN SEASONING AND FETTUCCINE)</div></div>
  <div class="item col-p1" style="top:342px"><div class="row">CHICKEN FLORENTINO<span class="dots"></span>15.99</div><div class="desc">(FETTUCCINE, SAUTEED CHICKEN, SUN-DRIED TOMATO, ALFREDO SAUCE, SPINACH, ARTICHOKE AND PARMESAN)</div></div>
  <div class="item col-p1" style="top:376px"><div class="row">CHICKEN PENNE PASTA<span class="dots"></span>15.99</div><div class="desc">(CHICKEN WITH MUSHRIIMS, SUN-DRIED TOMATO, CREAMY ALFREDO WITH PESTO SAUCE)</div></div>
  <div class="item col-p1" style="top:410px"><div class="row">CHICKEN PARMIGIANA<span class="dots"></span>15.99</div><div class="desc">(BREADED CHICKEN, MARINARA, CHEESE AND SPAGHETTI)</div></div>
  <div class="item col-p1" style="top:444px"><div class="row">EGGPLANT PARMIGIANA<span class="dots"></span>15.99</div><div class="desc">(EGGPLANT PARMIGIANA, MARINARA, CHEESE AND SPAGHETTI)</div></div>
  <div class="item col-p1" style="top:478px"><div class="row">CHEESE MANICOTTI<span class="dots"></span>15.99</div><div class="desc">(ROLLED PASTA SUFFED WITH RICOTTA, PARMESAN AND MOZZARELLA, BAKED WITH MARINARA)</div></div>
  <div class="item col-p1" style="top:513px"><div class="row">CHICKEN BROCCOLI PASTA<span class="dots"></span>15.99</div><div class="desc">(CHICKEN, BROCCOLI, PENNE, ALFREDO AND PESTO)</div></div>

  <div class="item col-p2" style="top:248px"><div class="row">LUNARIA SPECIALTY<span class="dots"></span>16.99</div><div class="desc">(GRILLED SHRIMPS, CHICKEN AND BEEF WITH PENNE IN OUR CAJUN ALFREDO SAUCE WITH DICED PEPPER)</div></div>
  <div class="item col-p2" style="top:282px"><div class="row">PASTA ITALIANO<span class="dots"></span>15.99</div><div class="desc">(GRILLED CHICKEN AND PENNE WITH ALFREDO SAUCE, PARMESAN AND FETA WITH MUSHROOMS AND SUN-DRIED TOMATOES)</div></div>
  <div class="item col-p2" style="top:324px"><div class="row">SEAFOOD FETTUCCINE ALFREDO<span class="dots"></span>15.99</div><div class="desc">(SHRIMP, CRABMEAT, MUSHROOMS, CHEESE, ALFREDO SAUCE AND FETTUCCINE)</div></div>
  <div class="item col-p2" style="top:358px"><div class="row">GRILLED SLAMON<span class="dots"></span>15.99</div></div>
  <div class="item col-p2" style="top:376px"><div class="row">CHICKEN PICATTA<span class="dots"></span>15.99</div><div class="desc">(GRILLED CHICKEN IN OUR HOMEMADE PICCATA SAUCE, WHITE WINE, BUTTER, GARLIC, CAPERS7LEMON SAUCE)</div></div>
  <div class="item col-p2" style="top:410px"><div class="row">SHRIMP ALFREDO<span class="dots"></span>15.99</div><div class="desc">(GRILLED SHRIMP, ALFREDO SAUCE,CHEESE, FETTUCCINE)</div></div>
  <div class="item col-p2" style="top:444px"><div class="row">CAJUN SHRIMP ALFREDO<span class="dots"></span>12.99</div><div class="desc">(GRILLED SHRIPM, ALFREDO SAUCE, CAJUN SEASONING, FETTUCCINE)</div></div>
  <p class="note" style="left:602px;top:486px;width:180px">All pastas sauces are made fresh daily from scratch in-house. All pastas served with bread sticks. Add a house salad for $3.00</p>
</section>
</body>
</html>
```